Web re-design project www.varvikworks.com

We need a corporate website for a startup company called Varvik Works. The company offers web-based worksite management system for big construction companies. In short, replacing annoying papers with iPads.
We need the site main page to provide basic overview of the company and then inner page layout for displaying news and detailed information about products.
Currently we have a site up at:
http://www.varvikworks.com/en/main
but as you can see the graphic design is a bit lacking in quality(implemented by a tech guy :)
We need you to pimp that web site design up!
There is possibility for more freelance work in the future related to our web products, slide show designs and printed marketing materials.
Our main product is PELMO. You can find a short presentation about what it does here:
http://www.varvikworks.com/en/pelmo
Here you can find packages of images and screenshots related to our company:
https://files.stashbin.example/u/7720419/varvik_images.zip
https://files.stashbin.example/u/7720419/varvikworks%20images2.zip
Product logo svg can be found here:
https://files.stashbin.example/u/7720419/PELMO-logo.svg
Your are not forced to use those images, but hopefully there will be something that is useful.
Hope to hear from you guys soon!
Cheers,
Aarni
Update:
We will be using PELMO logo as the company brand. I don't like our current Varvik Works company logo, so that doesn't need to be included in the site design.
Update 2:
I like website designs that are "light", elegant and pretty simplistic. One example is our product login page (screenshot included in files).
Update 3:
Sites from the same industry / type of products:
http://www.rakomesta.fi/
http://www.brellinsurvey.com/products/software/network-applications/gradelane-3d
http://www.quostar.com/construction/heavy-civil/software-solutions/Linked-Crewfield.aspx?dtID=overview&
Target Market(s)
Target audience for the website is companies in the construction sector, and possibly corporate investors
Industry/Entity Type
Graphic Design
Look and feel

```html
<!DOCTYPE html>
<html lang="en">
<head>
<meta charset="utf-8">
<title>PELMO – Latest News</title>
<link rel="stylesheet" href="https://fonts.googleapis.com/css2?family=Mulish:ital,wght@0,400;0,600;0,700;0,800;1,800&display=swap">
<style>
  :root {
    --backdrop: #c6b8a5;
    --page: #ffffff;
    --taupe: #968b7b;
    --taupe-dark: #7f7566;
    --taupe-light: #b2a897;
    --footer: #8f8574;
    --heading: #3d3833;
    --title: #8a7f70;
    --body-text: #a0957f;
    --nav-text: #7d7467;
    --rule: #8c8478;
    --ink: #1c1c1c;
    --white: #ffffff;
  }
  * { box-sizing: border-box; margin: 0; padding: 0; }
  html, body {
    width: 1111px; height: 1200px; overflow: hidden;
    background: var(--backdrop);
    font-family: "Mulish", Arial, sans-serif;
  }
  .page {
    position: absolute; left: 48px; top: 0; width: 1011px; height: 1200px;
    background: var(--page);
    box-shadow: 0 0 14px rgba(80, 64, 44, 0.35);
  }
  .brand {
    position: absolute; left: 68px; top: 72px;
    font-size: 50px; font-weight: 600; letter-spacing: 1px; color: var(--ink);
  }
  .search {
    position: absolute; left: 738px; top: 43px; width: 202px; height: 29px;
    border: 1px solid #c9c2b7; display: flex;
  }
  .search-field {
    flex: 1; padding-left: 9px; font-size: 15px; line-height: 27px; color: #9b9384;
  }
  .search-button {
    width: 40px; height: 27px; background: #d8d1c6; border-left: 1px solid #c9c2b7;
    display: flex; align-items: center; justify-content: center;
  }
  .main-nav { position: absolute; top: 91px; left: 0; width: 100%; height: 41px; }
  .main-nav a {
    position: absolute; top: 0; height: 41px; line-height: 41px;
    font-size: 19px; font-weight: 600; color: var(--nav-text); text-decoration: none;
    transform: translateX(-50%); white-space: nowrap;
  }
  .main-nav a.current {
    width: 114px; text-align: center; color: var(--white);
    background: linear-gradient(#aea494, #8b8171);
    border: 1px solid #7b7263; box-shadow: inset 0 1px 0 #c9c0b2;
  }
  .section-title {
    position: absolute; left: 89px; top: 172px;
    font-size: 37px; font-weight: 800; font-style: italic; color: var(--heading);
  }
  .news-list {
    position: absolute; left: 88px; top: 227px; width: 852px;
    list-style: none; border-top: 1px solid var(--rule);
  }
  .news-item {
    position: relative; height: 111.3px; border-bottom: 1px solid var(--rule);
  }
  .news-title {
    position: absolute; left: 2px; top: 15px;
    font-size: 17.5px; font-weight: 700; color: var(--title);
  }
  .news-summary {
    position: absolute; left: 2px; top: 46px; width: 680px;
    font-size: 16.3px; line-height: 20px; color: var(--body-text);
  }
  .news-date {
    position: absolute; right: 0; top: 12px; width: 117px; height: 32px;
    background: var(--taupe); color: #433c33;
    font-size: 18px; font-weight: 800; line-height: 32px; text-align: center;
  }
  .read-more {
    position: absolute; right: -2px; top: 55px; width: 121px; height: 33px;
    background: linear-gradient(#a69c8b, #8b8171);
    border: 1px solid #7b7263; box-shadow: inset 0 2px 0 #d2cabd;
    color: var(--white); font-size: 16px; font-weight: 700; line-height: 31px;
    text-align: center; text-decoration: none;
  }
  .pagination { position: absolute; top: 919px; left: 0; width: 100%; }
  .pagination a {
    position: absolute; top: 0; width: 47px; height: 33px;
    background: linear-gradient(#a69c8b, #887e6e);
    border: 1px solid #6f6759; box-shadow: inset 0 2px 0 #d2cabd;
    color: var(--white); font-size: 17px; font-weight: 800; line-height: 31px;
    text-align: center; text-decoration: none;
  }
  .pagination a.current {
    background: linear-gradient(#857b6b, #6d6456);
    box-shadow: inset 0 0 0 2px #b6ad9f;
  }
  .site-footer {
    position: absolute; left: 0; top: 980px; width: 1011px; height: 220px;
    background: var(--footer); color: var(--white);
  }
  .footer-column { position: absolute; top: 22px; }
  .footer-column h3 { font-size: 16px; font-weight: 800; line-height: 20px; margin-bottom: 3px; }
  .footer-column li { list-style: none; font-size: 15.5px; line-height: 19.6px; }
  .social-links { display: flex; gap: 4px; margin-top: 7px; }
  .social-links span {
    width: 36px; height: 35px; border-radius: 3px; background: #6f7f94;
    box-shadow: inset 0 0 0 1px rgba(255,255,255,0.35);
  }
  .assistance {
    position: absolute; top: 157px; left: 0; width: 100%;
    font-size: 15px; text-align: center; padding-right: 0;
    display: flex; justify-content: center; align-items: center; gap: 10px;
  }
  .assistance-dot { width: 13px; height: 13px; border-radius: 50%; background: #2fa9d8; }
  .copyright {
    position: absolute; top: 183px; left: 0; width: 100%;
    font-size: 15px; font-weight: 600; text-align: center;
  }
</style>
</head>
<body>
  <div class="page">
    <header>
      <div class="brand">PELMO</div>
      <div class="search">
        <span class="search-field">Search...</span>
        <span class="search-button">
          <svg width="16" height="16" viewBox="0 0 16 16" aria-hidden="true">
            <circle cx="6.5" cy="6.5" r="4.5" fill="none" stroke="#7d7467" stroke-width="2"/>
            <line x1="10" y1="10" x2="14.5" y2="14.5" stroke="#7d7467" stroke-width="2.6" stroke-linecap="round"/>
          </svg>
        </span>
      </div>
      <nav class="main-nav">
        <a href="#" style="left:483px">Home</a>
        <a href="#" style="left:633px">Products</a>
        <a href="#" class="current" style="left:773px">News</a>
        <a href="#" style="left:907px">Contact</a>
      </nav>
    </header>

    <main>
      <h1 class="section-title">Latest News</h1>
      <ul class="news-list">
        <li class="news-item">
          <h2 class="news-title">Welcome to our new website</h2>
          <p class="news-summary">Varvik Works new website has been launched. From these pages you can find information about PELMO cloud-based road construction service and other products from Varvik Works.</p>
          <span class="news-date">22. 11. 2012</span>
          <a class="read-more" href="#">Read more</a>
        </li>
        <li class="news-item">
          <h2 class="news-title">Welcome to our new website</h2>
          <p class="news-summary">Varvik Works new website has been launched. From these pages you can find information about PELMO cloud-based road construction service and other products from Varvik Works.</p>
          <span class="news-date">22. 11. 2012</span>
          <a class="read-more" href="#">Read more</a>
        </li>
        <li class="news-item">
          <h2 class="news-title">Welcome to our new website</h2>
          <p class="news-summary">Varvik Works new website has been launched. From these pages you can find information about PELMO cloud-based road construction service and other products from Varvik Works.</p>
          <span class="news-date">22. 11. 2012</span>
          <a class="read-more" href="#">Read more</a>
        </li>
        <li class="news-item">
          <h2 class="news-title">Welcome to our new website</h2>
          <p class="news-summary">Varvik Works new website has been launched. From these pages you can find information about PELMO cloud-based road construction service and other products from Varvik Works.</p>
          <span class="news-date">22. 11. 2012</span>
          <a class="read-more" href="#">Read more</a>
        </li>
        <li class="news-item">
          <h2 class="news-title">Welcome to our new website</h2>
          <p class="news-summary">Varvik Works new website has been launched. From these pages you can find information about PELMO cloud-based road construction service and other products from Varvik Works.</p>
          <span class="news-date">22. 11. 2012</span>
          <a class="read-more" href="#">Read more</a>
        </li>
        <li class="news-item">
          <h2 class="news-title">Welcome to our new website</h2>
          <p class="news-summary">Varvik Works new website has been launched. From these pages you can find information about PELMO cloud-based road construction service and other products from Varvik Works.</p>
          <span class="news-date">22. 11. 2012</span>
          <a class="read-more" href="#">Read more</a>
        </li>
      </ul>

      <nav class="pagination">
        <a href="#" style="left:377px">1</a>
        <a href="#" style="left:441px">2</a>
        <a href="#" class="current" style="left:507px">3</a>
        <a href="#" style="left:571px">4</a>
      </nav>
    </main>

    <footer class="site-footer">
      <div class="footer-column" style="left:60px">
        <h3>About us</h3>
        <ul><li>Company info</li><li>The Team</li><li>Careers</li><li>Privacy Policy</li></ul>
      </div>
      <div class="footer-column" style="left:244px">
        <h3>Services</h3>
        <ul><li>Structural Steels</li><li>Roofs</li><li>Walls</li><li>Foundations</li></ul>
      </div>
      <div class="footer-column" style="left:425px">
        <h3>Design Guidance</h3>
        <ul><li>Structural design</li><li>Flooring</li><li>Steel bridges</li><li>Envelope</li></ul>
      </div>
      <div class="footer-column" style="left:627px">
        <h3>Social Media</h3>
        <ul><li>Follow us on</li></ul>
        <div class="social-links" role="img" aria-label="Social network links">
          <span></span><span></span><span></span><span></span>
        </div>
      </div>
      <div class="footer-column" style="left:833px">
        <h3>Contact</h3>
        <ul><li>Partners</li><li>Contact</li><li>Site Map</li><li>Location</li></ul>
      </div>
      <p class="assistance">For assistance <span class="assistance-dot"></span> 1-877-V-0-RWK</p>
      <p class="copyright">Copyright © Varvik Works 2012</p>
    </footer>
  </div>
</body>
</html>
```